Hollow Birch Vintners Reserve Cabernet Sauvignon Wine Labels front and back

I need a front and back wine label. For a new RESERVE Cabernet Sauvignon wine. I am attaching the details and some ideas and possible images to use. But creativity is encouraged. This wine will be seen on wine shop and grocery store shelves so it needs to pop while appearing elegant and to be about $50/bottle of wine. The front and back labels should go together nicely. I would like some foil on the front, but not the back. We are trying to show the natural beauty of our vineyards and the elegance of our wines. We would like to invoke a feel of sustainability, proudly family owned and operated.

Target Market(s)

21-50 year olds, red wine drinkers, higher priced wine drinkers

Industry/Entity Type

Wine

Font styles to use
Serif
Script

Colors

Designer to choose only greyscale colors for use in the design.

Requirements
Must have
• Front Label with specified details and Back label with specified details. Foil banner on the front label that says " Family stewards of the land for 5 generations"the front label that says
Nice to have
• vineyard or winery background, have include a sample or example, some gold or bronze or silver accents

```html
<!DOCTYPE html>
<html lang="en">
<head>
<meta charset="utf-8">
<title>Hollow Birch Vintners – Reserve Cabernet Sauvignon Labels</title>
<link rel="stylesheet" href="https://fonts.googleapis.com/css2?family=Cinzel:wght@400;600&family=Cormorant+Garamond:ital,wght@0,400;0,600;1,400;1,600&family=Roboto+Condensed:wght@400;700&display=swap">
<style>
  :root {
    --page: #f3f1ee;
    --label-dark: #2b2622;
    --label-mid: #3a332d;
    --gold: #cfa968;
    --gold-soft: #b89a66;
    --copper: #b8643a;
    --copper-dark: #8e4a2a;
    --cream: #e9dfcf;
    --ink: #2a1c14;
  }
  * { box-sizing: border-box; margin: 0; padding: 0; }
  html, body { width: 1000px; height: 1200px; overflow: hidden; background: var(--page); }
  .canvas { position: relative; width: 1000px; height: 1200px; }

  .label {
    position: absolute;
    background: linear-gradient(180deg, var(--label-mid) 0%, var(--label-dark) 60%);
    border: 6px solid var(--copper);
    box-shadow: 0 6px 18px rgba(0,0,0,.18);
    overflow: hidden;
  }
  .label::before {
    content: ""; position: absolute; inset: 6px;
    border: 1.5px solid var(--gold-soft); pointer-events: none; z-index: 2;
  }

  /* FRONT */
  .front { left: 70px; top: 290px; width: 400px; height: 620px; text-align: center; }
  .ornament-rule { display: block; margin: 26px auto 0; }
  .brand-mark {
    display: block; width: 30px; height: 30px; margin: -22px auto 0;
    border: 2px solid var(--gold); background: var(--label-mid);
  }
  .brand-name {
    font-family: "Cinzel", serif; font-weight: 400; color: var(--gold);
    font-size: 42px; line-height: 1.08; letter-spacing: 1px; margin-top: 16px;
  }
  .tier {
    font-family: "Cormorant Garamond", serif; font-style: italic; color: var(--gold);
    font-size: 26px; letter-spacing: 2px; margin-top: 26px;
  }
  .varietal {
    font-family: "Cormorant Garamond", serif; color: var(--cream);
    font-size: 32px; line-height: 1.05;
  }
  .region {
    font-family: "Cormorant Garamond", serif; font-style: italic; color: var(--gold-soft);
    font-size: 17px; margin-top: 6px;
  }
  .vintage {
    font-family: "Cormorant Garamond", serif; font-style: italic; color: var(--cream);
    font-size: 24px; margin-top: 2px;
  }
  .vineyard-scene {
    position: absolute; left: 0; right: 0; bottom: 40px; height: 220px;
    background:
      radial-gradient(ellipse at 20% 40%, rgba(226,132,60,.9) 0%, rgba(226,132,60,0) 45%),
      radial-gradient(ellipse at 82% 45%, rgba(226,132,60,.85) 0%, rgba(226,132,60,0) 45%),
      linear-gradient(180deg, rgba(43,38,34,0) 0%, #7a4a2c 45%, #c0703a 100%);
  }
  .heritage-banner {
    position: absolute; left: 0; right: 0; bottom: 0; height: 40px; z-index: 3;
    background: linear-gradient(90deg, var(--copper-dark), var(--copper), var(--copper-dark));
    font-family: "Cormorant Garamond", serif; font-weight: 600; color: var(--ink);
    font-size: 12.5px; letter-spacing: 1.2px; text-transform: uppercase;
    display: flex; align-items: center; justify-content: center;
  }

  /* BACK */
  .back { left: 530px; top: 345px; width: 370px; height: 450px; padding: 18px 24px 0; }
  .back .brand-mark { width: 22px; height: 22px; margin: 4px auto 0; border-width: 1.5px; }
  .back .brand-name { font-size: 19px; text-align: center; margin-top: 6px; line-height: 1.1; }
  .story {
    font-family: "Cormorant Garamond", serif; color: var(--cream);
    font-size: 12.5px; line-height: 1.28; margin-top: 10px; text-align: justify;
  }
  .story .drop-cap {
    float: left; font-family: "Cinzel", serif; color: var(--gold);
    font-size: 36px; line-height: 30px; margin: 2px 5px 0 0;
  }
  .signoff {
    font-family: "Cormorant Garamond", serif; color: var(--cream); text-align: center;
    font-size: 12.5px; margin-top: 6px; line-height: 1.2;
  }
  .signoff .role { display: block; font-size: 10px; font-style: italic; color: var(--gold-soft); }
  .gov-warning {
    margin-top: 10px; width: 215px; border: 1px solid var(--cream); padding: 5px 7px;
    font-family: "Roboto Condensed", sans-serif; color: var(--cream); font-size: 8.5px; line-height: 1.25;
  }
  .gov-warning strong { display: block; font-size: 10px; margin-bottom: 2px; }
  .gov-warning p + p { margin-top: 2px; }
  .legal-row {
    display: flex; gap: 20px; margin-top: 10px;
    font-family: "Roboto Condensed", sans-serif; color: var(--cream); font-size: 8.5px; line-height: 1.25; text-transform: uppercase;
  }
  .legal-row .volume { font-size: 14px; font-weight: 700; display: block; line-height: 1.1; }
  .legal-row .producer { font-weight: 700; }
</style>
</head>
<body>
<main class="canvas">

  <section class="label front" aria-label="Front label">
    <svg class="ornament-rule" width="320" height="20" viewBox="0 0 320 20" aria-hidden="true">
      <path d="M10 10 H135 M185 10 H310" stroke="#cfa968" stroke-width="1.2" fill="none"/>
      <path d="M40 6 H135 M185 6 H280" stroke="#cfa968" stroke-width=".6" fill="none"/>
    </svg>
    <span class="brand-mark" aria-hidden="true"></span>
    <h1 class="brand-name">Hollow Birch<br>Vintners</h1>
    <p class="tier">RESERVE</p>
    <p class="varietal">Cabernet Sauvignon</p>
    <p class="region">Horse Heaven Hills</p>
    <p class="vintage">2022</p>
    <div class="vineyard-scene" role="img" aria-label="Copper foil engraving of vineyard rows and rolling hills framed by trees"></div>
    <div class="heritage-banner">Family stewards of the land for 5 generations</div>
  </section>

  <section class="label back" aria-label="Back label">
    <span class="brand-mark" aria-hidden="true"></span>
    <h2 class="brand-name">Hollow Birch<br>Vintners</h2>
    <p class="story"><span class="drop-cap">O</span>ur vineyards, nestled along the Columbia River in Washington state, flourish in a region celebrated for its long, hot days and cool, crisp nights. This area, rich in natural resources and fertile soils, imparts a unique essence of balance, structure, and elegance to our wines.</p>
    <p class="signoff">Cheers,<br>Maren Colby<span class="role">Winemaker</span></p>
    <div class="gov-warning">
      <strong>GOVERNMENT WARNING:</strong>
      <p>(1) According to the Surgeon General, women should not drink alcoholic beverages during pregnancy because of the risk of birth defects.</p>
      <p>(2) Consumption of alcoholic beverages impairs your ability to drive a car or operate machinery, and may cause health problems.</p>
    </div>
    <div class="legal-row">
      <p><span class="volume">750 ML</span>Contains sulfites<br>13% alc. by vol.</p>
      <p class="producer">Produced and bottled<br>by Quillmoor Wine Estates,<br>LLC, Tallow Bend WA, USA</p>
    </div>
  </section>

</main>
</body>
</html>
```